Wordpress Design Project

Tovimo Pathways is a social entrepreneurship program that organizes and leads development projects in and educational expeditions to Guatemala in order to promote economic development.

We want our website to convey our sustainable business model with colors (greens, yellows, organges,like our logo, etc.) that match our logo, which will be integrated throughout the site, as well as our slogan (Wander, Wonder, Widen your world, Walk the Way).

We want the entire site to appear simple and easy to navigate. We want our name and logo to be featured prominently at the top of our home page as well as our slogan with very large (revolving/changing) photographs featured below or as a background to the page. If possible we would like quotes, testimonials about our programs, or statistics on Guatemala to be printed over these photos.

The first of the sections headings displayed should be eXplore (About Tovimo) and underneath will appear our Mission and Philosophy, History, Advisory Board, and Founder information. The second should be eXperience with Our Approach, Our Partners here and abroad, Themed Trips, Pricing and Sample Trips, and the $5 Challenge. The third should be eXpect More (Benefits) with Online Store and Past Trips below. The remaining section header should be Request a Proposal.

Target Market(s)

U.S. and Canadian university students and professors and philanthropic or social entrepreneurship organizations

Requirements
Must have
• - include a space for the video on the homepage
- logo, company name and slogan, and large colorful photographs as listed in the description
Nice to have
• http://www.brightmarrow.org/
http://quillharborproject.org/
Should not have
• -not crowded or overwhelmed with text or visuals

```html
<!DOCTYPE html>
<html lang="en">
<head>
<meta charset="utf-8">
<title>Tovimo Pathways</title>
<link href="https://fonts.googleapis.com/css2?family=Open+Sans:wght@400;600;700&family=Poppins:wght@600&display=swap" rel="stylesheet">
<style>
:root{
  --green:#1e9447;
  --green-dark:#177a3a;
  --green-foot:#2a9a45;
  --lime:#c8dc2a;
  --brown:#4a2a1c;
  --brown-light:#6b3f2a;
  --grey-btn:#e4e4e4;
  --text:#555;
  --heading:#3b2a22;
  --page:#f3f3ee;
  --white:#fff;
}
*{margin:0;padding:0;box-sizing:border-box}
html,body{width:686px;height:1200px;overflow:hidden}
body{background:var(--page);font-family:"Open Sans",Arial,sans-serif;color:var(--text);font-size:7px;position:relative}
.abs{position:absolute}

/* hero */
.hero{left:0;top:0;width:686px;height:345px;background:linear-gradient(180deg,#2f4a2a 0%,#4d7a3c 30%,#6a8f55 55%,#3a5a33 80%,#2b3f27 100%)}
.hero-photo{left:36px;top:0;width:614px;height:345px;background:radial-gradient(ellipse at 45% 40%,#9fbf8c 0%,#5f8c4a 40%,#2f4f2a 100%)}
.logo{left:80px;top:28px;width:96px;height:96px;border-radius:50%;background:var(--white);border:4px solid var(--green);display:flex;align-items:center;justify-content:center;font-weight:700;font-size:17px;color:var(--green)}
.nav{left:178px;top:75px;width:436px;height:24px;background:var(--white);display:flex;box-shadow:0 1px 3px rgba(0,0,0,.3)}
.nav a{font-family:"Open Sans",sans-serif;font-weight:700;font-size:7.5px;color:#444;text-decoration:none;text-transform:uppercase;display:flex;align-items:center;padding:0 12px;border-right:1px solid #ddd}
.nav a.active{background:var(--green);color:var(--white)}
.nav a:last-child{border:0;margin-left:auto}
.social-label{left:436px;top:36px;color:#eee;font-size:6px}
.social-icons{left:436px;top:46px;display:flex;gap:3px}
.social-icons span{width:11px;height:11px;background:#f2f2f2;border-radius:2px}
.account{left:516px;top:36px;color:#eee;font-size:6px}
.search{left:516px;top:47px;width:92px;height:13px;background:var(--white);border-radius:2px;font-size:6px;color:#999;padding:2px 4px}
.slogan{left:74px;top:146px;width:244px;white-space:nowrap;font-family:"Poppins",sans-serif;font-weight:600;font-size:26px;line-height:36px;color:var(--white);letter-spacing:-.6px}
.cta{left:74px;top:266px;width:200px;height:36px;background:var(--brown-light);border-radius:3px;color:var(--white);font-family:"Poppins",sans-serif;font-size:14px;display:flex;align-items:center;padding-left:22px;gap:8px}
.video{left:325px;top:123px;width:289px;height:196px;background:linear-gradient(180deg,#dfe3dc,#b7bcb4);box-shadow:0 2px 6px rgba(0,0,0,.4)}
.video-bar{left:325px;top:300px;width:289px;height:19px;background:#1a1a1a;color:#ccc;font-size:6px}
.hero-arrow{top:208px}

/* content */
.content{left:36px;top:345px;width:614px;height:600px;background:var(--white)}
.divider{left:452px;top:350px;width:1px;height:590px;background:#e5e5e5}
.sec-title{font-weight:600;font-size:12px;color:var(--green);display:flex;align-items:center;gap:6px}
.sec-title .tag{background:var(--lime);color:var(--green-dark);font-size:6.5px;font-weight:400;padding:1px 5px 1px 7px;clip-path:polygon(5px 0,100% 0,100% 100%,5px 100%,0 50%)}
.rule{height:1px;background:#ddd}
.card{top:425px;width:86px;height:84px;border:1px solid var(--green);border-radius:3px;color:var(--green);font-size:7px;font-weight:600;text-align:center;display:flex;flex-direction:column;align-items:center;justify-content:flex-end;padding-bottom:22px;gap:8px}
.card.active{background:var(--green);color:var(--white);height:92px;clip-path:polygon(0 0,100% 0,100% 84px,50% 92px,0 84px)}
.ticks{list-style:none;left:78px;width:350px}
.ticks li{position:relative;padding-left:14px;margin-bottom:9px;line-height:9px;font-size:6.5px}
.ticks li::before{content:"";position:absolute;left:0;top:1px;width:8px;height:8px;border-radius:50%;background:var(--lime)}
.ticks li::after{content:"";position:absolute;left:2.5px;top:3px;width:3px;height:2px;border-left:1px solid var(--white);border-bottom:1px solid var(--white);transform:rotate(-45deg)}
.pbtn{width:174px;height:20px;background:var(--grey-btn);color:#555;font-weight:600;font-size:7px;display:flex;align-items:center;justify-content:space-between;padding:0 8px}
.pbtn i{width:9px;height:9px;border-radius:50%;background:#bbb}
.pbtn.dark{background:var(--brown-light);color:var(--white)}
.pbtn.dark i{background:var(--white)}
.sub-title{font-size:9px;font-weight:600;color:#333;display:flex;align-items:center;gap:6px}
.trip{display:flex;gap:6px;font-size:6.5px;line-height:8px;width:160px}
.trip span.thumb{flex:0 0 16px;height:12px;background:#a6987e}
.trip b{color:#222}
.sbtn{height:18px;background:var(--brown-light);color:var(--white);font-size:7px;border-radius:2px;display:flex;align-items:center;padding:0 6px}
.side-title{font-weight:600;font-size:12px;color:var(--heading)}
.bbtn{width:140px;height:22px;background:var(--brown-light);color:var(--white);font-weight:600;font-size:7.5px;border-radius:2px;display:flex;align-items:center;justify-content:space-between;padding:0 8px}
.bbtn i{width:9px;height:9px;border-radius:50%;background:var(--white)}
.proposal{left:474px;top:557px;width:140px;height:213px;background:linear-gradient(180deg,var(--green) 0%,#3f9a3c 100%);padding:12px 8px}
.proposal h3{color:var(--white);font-weight:600;font-size:12px}
.field{background:var(--white);height:15px;margin-top:5px;font-size:6px;color:#999;padding:3px 6px}
.badge{width:70px;height:18px;border:1px solid #ddd;background:#fafafa}
.badge-row{display:flex;gap:5px}
.partner-sub{font-size:8px;font-weight:600;color:var(--heading)}

/* footer */
.footer{left:36px;top:945px;width:614px;height:255px;background:linear-gradient(180deg,#239a47,#3c9a3a)}
.fcol{top:985px;color:var(--white)}
.fcol h4{font-weight:400;font-size:10px;padding-bottom:7px;border-bottom:1px solid rgba(255,255,255,.5);width:118px;margin-bottom:8px}
.fcol a{display:block;color:var(--white);text-decoration:none;font-size:6.5px;line-height:14.2px}
.fcol.icons a{padding-left:11px;position:relative}
.fcol.icons a::before{content:"";position:absolute;left:0;top:4px;width:6px;height:6px;border-radius:50%;background:rgba(255,255,255,.8)}
.fcol p{font-size:6.5px;line-height:9px;width:118px}
.flogo{left:510px;top:1088px;width:54px;height:54px;border-radius:50%;background:var(--white);border:3px solid var(--green-dark);display:flex;align-items:center;justify-content:center;font-weight:700;font-size:9px;color:var(--green)}
.fsmall{color:var(--white);font-size:5.5px}
.frule{left:74px;top:1163px;width:540px;height:1px;background:rgba(255,255,255,.4)}
</style>
</head>
<body>

<!-- HERO -->
<div class="abs hero"></div>
<div class="abs hero-photo" role="img" aria-label="Large photograph of a green jungle river and waterfall in Guatemala"></div>

<div class="abs logo">Tovimo</div>

<div class="abs social-label">Social Sharing</div>
<div class="abs social-icons"><span></span><span></span><span></span><span></span><span></span></div>
<div class="abs account">Login | Register | Site Map</div>
<div class="abs search">Search</div>

<nav class="abs nav">
  <a href="#">Mission</a>
  <a href="#" class="active">Programs and Expeditions</a>
  <a href="#">Our Partners</a>
  <a href="#">Our Products</a>
  <a href="#">Contact Us</a>
</nav>

<div class="abs slogan">Wander<br>Wonder<br>Widen your world</div>
<div class="abs cta">Walk the Way
  <svg width="12" height="12" viewBox="0 0 12 12"><circle cx="6" cy="6" r="6" fill="#fff"/><path d="M5 3.5 7.5 6 5 8.5" stroke="#6b3f2a" stroke-width="1.6" fill="none"/></svg>
</div>

<div class="abs video" role="img" aria-label="Embedded video player showing the Tovimo Pathways project introduction"></div>
<div class="abs video-bar">
  <svg width="289" height="19" viewBox="0 0 289 19">
    <rect x="0" y="0" width="289" height="3" fill="#444"/>
    <rect x="0" y="0" width="82" height="3" fill="#c8202a"/>
    <circle cx="82" cy="1.5" r="3" fill="#ddd"/>
    <rect x="15" y="8" width="2" height="7" fill="#ccc"/><rect x="19" y="8" width="2" height="7" fill="#ccc"/>
    <path d="M38 10h3l4-3v9l-4-3h-3z" fill="#ccc"/>
    <text x="55" y="14" fill="#ccc" font-size="6" font-family="Open Sans,sans-serif">0:02 / 0:10</text>
    <text x="240" y="14" fill="#ccc" font-size="6" font-family="Open Sans,sans-serif">720p</text>
    <rect x="264" y="8" width="6" height="6" fill="none" stroke="#ccc"/>
    <rect x="276" y="8" width="7" height="6" fill="none" stroke="#ccc"/>
  </svg>
</div>

<svg class="abs hero-arrow" style="left:46px" width="12" height="26" viewBox="0 0 12 26"><path d="M10 2 2 13l8 11" stroke="#fff" stroke-opacity=".7" stroke-width="2" fill="none"/></svg>
<svg class="abs hero-arrow" style="left:628px" width="12" height="26" viewBox="0 0 12 26"><path d="M2 2l8 11-8 11" stroke="#fff" stroke-opacity=".7" stroke-width="2" fill="none"/></svg>

<!-- CONTENT -->
<div class="abs content"></div>
<div class="abs divider"></div>

<!-- About -->
<div class="abs sec-title" style="left:74px;top:397px">About Tovimo <span class="tag">Wander</span></div>
<div class="abs rule" style="left:74px;top:416px;width:352px"></div>

<div class="abs card active" style="left:74px">
  <svg width="22" height="20" viewBox="0 0 22 20"><path d="M1 9 21 1l-7 18-3-7z" fill="#fff"/></svg>
  <span>Our Mission and<br>Philosophy</span>
</div>
<div class="abs card" style="left:164px">
  <svg width="20" height="20" viewBox="0 0 20 20"><rect x="2" y="3" width="15" height="15" rx="2" fill="none" stroke="#1e9447" stroke-width="2"/><path d="M7 13l1-3 7-7 2 2-7 7z" fill="#1e9447"/></svg>
  <span>History</span>
</div>
<div class="abs card" style="left:253px">
  <svg width="28" height="20" viewBox="0 0 28 20"><circle cx="9" cy="5" r="4" fill="#1e9447"/><circle cx="19" cy="5" r="4" fill="#1e9447"/><path d="M1 19c0-6 4-8 8-8s8 2 8 8zM13 19c0-5 3-8 6-8 4 0 8 2 8 8z" fill="#1e9447"/></svg>
  <span>Advisory Board</span>
</div>
<div class="abs card" style="left:342px">
  <svg width="30" height="20" viewBox="0 0 30 20"><ellipse cx="10" cy="9" rx="9" ry="7" fill="#1e9447"/><ellipse cx="20" cy="10" rx="9" ry="7" fill="#1e9447"/></svg>
  <span>From the Founder</span>
</div>

<ul class="abs ticks" style="top:533px">
  <li>Because we believe that the best way to unlock your unique gifts and potential is by helping others unlock theirs.</li>
  <li>Tovimo Pathways is a social enterprise that utilizes social entrepreneurship principles and systems in order to "unlock" people's human potential in ways that support themselves, their families, and initiates positive social change.</li>
  <li>Tovimo Pathways organizes and leads expeditions to Guatemala in order to unlock human potential for both participant and recipient.</li>
</ul>

<!-- Programs -->
<div class="abs sec-title" style="left:74px;top:649px">Programs / Pricing <span class="tag">Wonder</span></div>
<div class="abs rule" style="left:74px;top:668px;width:352px"></div>
<div class="abs pbtn dark" style="left:74px;top:673px">Our Approach<i></i></div>
<div class="abs pbtn" style="left:254px;top:673px">Our Partners here and Abroad<i></i></div>
<div class="abs pbtn" style="left:74px;top:699px">Themed Trips<i></i></div>
<div class="abs pbtn" style="left:254px;top:699px">Pricing and Sample Trips<i></i></div>
<div class="abs pbtn" style="left:74px;top:724px">Past Trips Summaries<i></i></div>
<div class="abs pbtn" style="left:254px;top:724px">The $5 Challenge<i></i></div>

<!-- Benefits -->
<div class="abs sec-title" style="left:74px;top:776px">Benefits <span class="tag">Widen your world</span></div>
<div class="abs rule" style="left:74px;top:795px;width:352px"></div>

<div class="abs sub-title" style="left:74px;top:812px">
  <svg width="14" height="12" viewBox="0 0 14 12"><path d="M0 1h3l2 7h7l2-5H4" stroke="#4a2a1c" stroke-width="1.4" fill="none"/><circle cx="6" cy="10.5" r="1.3" fill="#4a2a1c"/><circle cx="11" cy="10.5" r="1.3" fill="#4a2a1c"/></svg>
  Online Store
</div>
<ul class="abs ticks" style="top:839px;width:170px">
  <li style="margin-bottom:7px">Aenean commodo ligula Lorem ipsum</li>
  <li style="margin-bottom:7px">Cum sociis natoque penatibus et magnis</li>
  <li style="margin-bottom:7px">Lorem ipsum dolor sit amet, consectetuer</li>
  <li style="margin-bottom:7px">Cum sociis natoque penatibus</li>
</ul>
<div class="abs" style="left:241px;top:812px;width:1px;height:110px;background:#ddd"></div>

<div class="abs sub-title" style="left:264px;top:810px">
  <svg width="14" height="12" viewBox="0 0 14 12"><rect x="0" y="2" width="14" height="10" rx="1" fill="#4a2a1c"/><rect x="4" y="0" width="6" height="3" fill="#4a2a1c"/><circle cx="7" cy="7" r="2.5" fill="#fff"/></svg>
  Past Trips
</div>
<div class="abs trip" style="left:264px;top:836px"><span class="thumb" role="img" aria-label="Trip thumbnail photo"></span><div><b>Aenean commodo</b> ligula Lorem ipsum dolor - <b>More</b> | 13 June 2012</div></div>
<div class="abs trip" style="left:264px;top:858px"><span class="thumb" role="img" aria-label="Trip thumbnail photo" style="background:#7a86a6"></span><div><b>Cum sociis natoque</b> penatibus et magnis dis parturient montes - <b>More</b> | 13 June 2012</div></div>
<div class="abs sbtn" style="left:264px;top:885px">Contact Our Team</div>
<div class="abs sbtn" style="left:340px;top:885px">Request a Proposal</div>

<!-- Sidebar -->
<div class="abs side-title" style="left:474px;top:396px">Tovimo Testimonials</div>
<div class="abs rule" style="left:474px;top:416px;width:140px"></div>
<div class="abs" role="img" aria-label="Portrait photo of testimonial author" style="left:474px;top:424px;width:28px;height:28px;background:#c9b8a0;border:1px solid #ddd"></div>
<div class="abs" style="left:510px;top:428px;font-weight:700;font-size:8px;color:#333">Marla Quenby</div>
<div class="abs" style="left:510px;top:440px;font-size:6.5px;color:var(--green)">Advisor - Australia</div>
<p class="abs" style="left:474px;top:458px;width:140px;font-size:6.5px;line-height:9px">Lorem ipsum dolor sit amet, consectetuer adipiscing elit. Aenean commodo ligula eget dolor. Aenean massa. Cum sociis natoque penatibus et magnis dis parturient montes, nascetur ridiculus mus.</p>
<div class="abs bbtn" style="left:474px;top:512px">All Testimonials<i></i></div>

<div class="abs proposal">
  <h3>Request a Proposal</h3>
  <div style="height:1px;background:rgba(255,255,255,.5);margin:8px 0 8px"></div>
  <div class="field">Your Name</div>
  <div class="field">Enter Email</div>
  <div class="field" style="height:64px">Message</div>
  <div class="bbtn" style="width:124px;height:18px;margin-top:8px;font-size:7px">Send Request<i></i></div>
</div>

<div class="abs side-title" style="left:474px;top:798px">Tovimo Partners</div>
<div class="abs rule" style="left:474px;top:818px;width:140px"></div>
<div class="abs partner-sub" style="left:474px;top:834px">Partners in Guatemala</div>
<div class="abs badge-row" style="left:474px;top:848px"><div class="badge"></div><div class="badge"></div></div>
<div class="abs partner-sub" style="left:474px;top:876px">Our Partners Abroad</div>
<div class="abs badge-row" style="left:474px;top:890px"><div class="badge"></div><div class="badge"></div></div>

<!-- FOOTER -->
<footer>
<div class="abs footer"></div>
<div class="abs fcol" style="left:74px">
  <h4>Tovimo Pathways</h4>
  <a href="#">Mission</a><a href="#">Programs</a><a href="#">Social Enterprise</a><a href="#">Products</a><a href="#">Travel &amp; Culture</a><a href="#">Speaking Circuits</a><a href="#">About Tovimo</a>
</div>
<div class="abs fcol" style="left:208px">
  <h4>Useful Links</h4>
  <a href="#">Newsletter</a><a href="#">Blog</a><a href="#">Partners in Guatemala</a><a href="#">Partners Abroad</a><a href="#">See Brochure</a><a href="#">Testimonials</a><a href="#">Benefits</a>
</div>
<div class="abs fcol icons" style="left:341px">
  <h4>Get Connet with Us</h4>
  <a href="#">Contact Us</a><a href="#">Campfire</a><a href="#">Chirpline</a><a href="#">Circlespace</a><a href="#">Workweave</a><a href="#">RSS Feed</a>
</div>
<div class="abs fcol" style="left:476px">
  <h4>Guatemala Profile</h4>
  <p>Lorem ipsum dolor sit amet, consectetuer adipiscing elit. Aenean commodo ligula eget dolor. Aenean massa. Cum sociis natoque</p>
</div>
<div class="abs flogo">Tovimo</div>
<div class="abs fsmall" style="left:74px;top:1143px">The Tovimo Pathways, 412 Fernbrook Lane Alderton PA, 17201 USA</div>
<div class="abs frule"></div>
<div class="abs fsmall" style="left:74px;top:1170px">All Right Reserve Copyright © 2012 With Tovimo Pathways, Privacy Policy | Terms of Use</div>
<div class="abs fsmall" style="left:532px;top:1170px">Powered By : Lumenvale Studio</div>
</footer>

</body>
</html>
```